Postcard design to acquire new clients for my Property Management Company

I'm looking for a postcard design that I can send to prospective clients detailing information about my company and services.
Postcard should be eye catching and contain information from www.brightkeeplm.com. I've provided a few screen shots for the most important information and my logo.
Target Market(s)
Real Estate
Industry/Entity Type
Real Estate
Font styles to use
Sans Serif
Requirements
Must have
- Must be eye catching!! this will be a direct mail piece - I'd like for the card to be read and not tossed in the trash immediately.
Design que from the logo.
A place to write / print the receipts name and address.
our physical address - 2287 Marden Lane, Lubbock, TX 79382.
Should not have
- the contact information on the business card is not accurate - please use info from website.

```html
<!DOCTYPE html>
<html lang="en">
<head>
<meta charset="utf-8">
<title>Brightkeep Property Management – Postcard</title>
<link href="https://fonts.googleapis.com/css2?family=Montserrat:wght@300;400;500;600;700;800&display=swap" rel="stylesheet">
<style>
  :root{
    --navy:#1b4582;
    --ink:#3b3f46;
    --grey:#6d7178;
    --line:#b9bcc2;
    --panel:#e9eaee;
    --icon-ring:#5b5f66;
    --paper:#ffffff;
    --backdrop:#d9d7d8;
    --photo-a:#4d5a63;
    --photo-b:#a9b2b4;
  }
  *{box-sizing:border-box;margin:0;padding:0}
  html,body{width:1200px;height:867px;overflow:hidden}
  body{background:var(--backdrop);font-family:"Montserrat",Arial,sans-serif;position:relative}

  .postcard{position:absolute;top:238px;width:570px;height:390px;background:var(--paper);box-shadow:0 6px 20px rgba(0,0,0,.15);overflow:hidden}
  .postcard--back{left:20px}
  .postcard--front{left:610px}

  /* front */
  .brand{position:absolute;left:38px;top:32px;color:var(--navy)}
  .brand__name{font-size:23px;font-weight:800;letter-spacing:2px;line-height:1}
  .brand__tag{font-size:9px;font-weight:500;letter-spacing:1.6px;margin-top:3px}
  .headline{position:absolute;left:38px;top:96px}
  .headline__lead{font-size:15px;font-weight:400;color:var(--grey);letter-spacing:.3px}
  .headline__main{font-size:33px;font-weight:800;color:var(--navy);line-height:.98;letter-spacing:-.3px}
  .headline__tail{font-size:17px;font-weight:400;color:var(--grey)}
  .headline__rule{width:56px;height:3px;background:var(--navy);margin-top:8px}
  .warning{position:absolute;left:38px;top:238px;width:185px;font-size:9.5px;line-height:1.35;color:var(--ink)}
  .cta{position:absolute;left:30px;bottom:32px}
  .cta__label{font-size:16px;font-weight:700;color:var(--ink);letter-spacing:.2px}
  .cta__phone{display:inline-block;margin-top:4px;padding:3px 14px;border-radius:20px;background:var(--navy);color:#fff;font-size:22px;font-weight:700}
  .cta__web{font-size:14.5px;font-weight:700;color:var(--ink);margin-top:5px}
  .cta__address{font-size:9.5px;font-weight:500;color:var(--grey);margin-top:3px}
  .photo-art{position:absolute;right:0;top:0;width:320px;height:390px}

  /* back */
  .offer{position:absolute;left:32px;top:28px;font-size:16px;font-weight:800;line-height:1.12;color:var(--ink)}
  .offer__soft{font-weight:500}
  .offer__accent{color:var(--navy)}
  .services{position:absolute;left:24px;top:96px;width:310px;height:166px;background:var(--panel)}
  .services__band{height:22px;background:var(--navy);color:#fff;font-size:10px;font-weight:600;letter-spacing:.6px;padding:5px 14px;width:150px;clip-path:polygon(0 0,88% 0,100% 100%,0 100%)}
  .services__grid{display:grid;grid-template-columns:repeat(4,1fr);row-gap:8px;padding:12px 10px 0}
  .service{text-align:center;font-size:7px;color:var(--ink);line-height:1.2}
  .service svg{display:block;margin:0 auto 3px;width:32px;height:32px}
  .cta--back{left:28px;bottom:16px}

  .mailing{position:absolute;left:362px;top:24px;width:184px;height:342px;border-left:1px solid var(--line);padding-left:18px}
  .mailing__stamp{position:absolute;right:0;top:0;width:56px;height:66px;border:1.5px dashed var(--line)}
  .mailing__label{position:absolute;left:18px;top:176px;font-size:8px;font-weight:600;letter-spacing:1px;color:var(--grey)}
  .mailing__lines{position:absolute;left:18px;right:0;top:200px}
  .mailing__line{height:1px;background:var(--line);margin-bottom:26px}
</style>
</head>
<body>

<section class="postcard postcard--back" aria-label="Postcard back">
  <h2 class="offer"><span class="offer__soft">WE OFFER</span><br>FULL-SERVICE <span class="offer__accent">PROPERTY<br>MANAGEMENT</span> SOLUTIONS</h2>

  <div class="services">
    <div class="services__band">OUR SERVICES</div>
    <div class="services__grid">
      <div class="service"><svg viewBox="0 0 32 32"><circle cx="16" cy="16" r="14" fill="#fff" stroke="var(--icon-ring)" stroke-width="2"/><path d="M9 16l7-6 7 6v7h-5v-4h-4v4H9z" fill="var(--icon-ring)"/></svg>Property<br>Marketing</div>
      <div class="service"><svg viewBox="0 0 32 32"><circle cx="16" cy="16" r="14" fill="#fff" stroke="var(--icon-ring)" stroke-width="2"/><circle cx="11" cy="13" r="2.5" fill="var(--icon-ring)"/><circle cx="21" cy="13" r="2.5" fill="var(--icon-ring)"/><circle cx="16" cy="12" r="3" fill="var(--icon-ring)"/><path d="M8 21a3 3 0 0 1 6 0zM18 21a3 3 0 0 1 6 0zM12 22a4 4 0 0 1 8 0z" fill="var(--icon-ring)"/></svg>Tenant<br>Screening</div>
      <div class="service"><svg viewBox="0 0 32 32"><circle cx="16" cy="16" r="14" fill="#fff" stroke="var(--icon-ring)" stroke-width="2"/><text x="16" y="22" text-anchor="middle" font-size="16" font-weight="700" fill="var(--icon-ring)" font-family="Montserrat,sans-serif">$</text></svg>Rent<br>Collection</div>
      <div class="service"><svg viewBox="0 0 32 32"><circle cx="16" cy="16" r="14" fill="#fff" stroke="var(--icon-ring)" stroke-width="2"/><rect x="10" y="9" width="12" height="5" rx="1" fill="var(--icon-ring)"/><rect x="15" y="13" width="2.5" height="11" fill="var(--icon-ring)"/></svg>Maintenance</div>
      <div class="service"><svg viewBox="0 0 32 32"><circle cx="16" cy="16" r="14" fill="#fff" stroke="var(--icon-ring)" stroke-width="2"/><circle cx="14" cy="14" r="5" fill="none" stroke="var(--icon-ring)" stroke-width="2.2"/><path d="M18 18l5 5" stroke="var(--icon-ring)" stroke-width="2.6"/></svg>Property<br>Inspections</div>
      <div class="service"><svg viewBox="0 0 32 32"><circle cx="16" cy="16" r="14" fill="#fff" stroke="var(--icon-ring)" stroke-width="2"/><rect x="10" y="17" width="3" height="6" fill="var(--icon-ring)"/><rect x="14.5" y="13" width="3" height="10" fill="var(--icon-ring)"/><rect x="19" y="10" width="3" height="13" fill="var(--icon-ring)"/></svg>Financial<br>Reporting</div>
      <div class="service"><svg viewBox="0 0 32 32"><circle cx="16" cy="16" r="14" fill="#fff" stroke="var(--icon-ring)" stroke-width="2"/><path d="M16 8l6 2.5v5c0 4-3 6.5-6 8-3-1.5-6-4-6-8v-5z" fill="var(--icon-ring)"/></svg>Evictions</div>
      <div class="service"><svg viewBox="0 0 32 32"><circle cx="16" cy="16" r="14" fill="#fff" stroke="var(--icon-ring)" stroke-width="2"/><path d="M16 9v13M10 11h12M12 23h8" stroke="var(--icon-ring)" stroke-width="1.8"/><path d="M8 17l2-6 2 6zM20 17l2-6 2 6z" fill="var(--icon-ring)"/></svg>Legal<br>Guidance</div>
    </div>
  </div>

  <div class="cta cta--back">
    <div class="cta__label">GIVE US A CALL NOW</div>
    <div class="cta__phone">(806) 555-0148</div>
    <div class="cta__web">www.brightkeeplm.com</div>
    <div class="cta__address">2287 Marden Lane, Lubbock, TX 79382</div>
  </div>

  <div class="mailing" aria-label="Recipient address area">
    <div class="mailing__stamp"></div>
    <div class="mailing__label">TO:</div>
    <div class="mailing__lines">
      <div class="mailing__line"></div>
      <div class="mailing__line"></div>
      <div class="mailing__line"></div>
      <div class="mailing__line"></div>
    </div>
  </div>
</section>

<section class="postcard postcard--front" aria-label="Postcard front">
  <div class="brand">
    <div class="brand__name">BRIGHTKEEP</div>
    <div class="brand__tag">PROPERTY MANAGEMENT</div>
  </div>

  <h1 class="headline">
    <div class="headline__lead">CHOOSE THE RIGHT</div>
    <div class="headline__main">PROPERTY<br>MANAGEMENT</div>
    <div class="headline__tail">SYSTEM</div>
    <div class="headline__rule"></div>
  </h1>

  <p class="warning">Selecting the wrong manager could be your costliest mistake ever.</p>

  <div class="cta">
    <div class="cta__label">GIVE US A CALL NOW</div>
    <div class="cta__phone">(806) 555-0148</div>
    <div class="cta__web">www.brightkeeplm.com</div>
  </div>

  <svg class="photo-art" viewBox="0 0 320 390">
    <defs>
      <linearGradient id="photoTone" x1="0" y1="0" x2="1" y2="1">
        <stop offset="0" stop-color="var(--photo-a)"/>
        <stop offset="1" stop-color="var(--photo-b)"/>
      </linearGradient>
    </defs>
    <g role="img" aria-label="Photo of two smiling businessmen reviewing a tablet in a bright lounge">
      <polygon points="90,40 260,40 170,390 0,390" fill="url(#photoTone)"/>
      <polygon points="260,40 320,40 320,390 180,390" fill="url(#photoTone)"/>
    </g>
    <polygon points="258,40 320,40 320,160" fill="var(--navy)"/>
    <polygon points="262,150 300,390 225,390" fill="var(--paper)"/>
    <polygon points="250,60 268,60 190,390 172,390" fill="var(--paper)"/>
  </svg>
</section>

</body>
</html>
```